Diet, Exercise, & Friends are Associated with Parkinson's disease Progression

We are researchers looking for modifiable variables associated with different rates of Parkinson's disease (PD) progression. This is a novel scale: www.VELQAN.org -- higher scores are associated with worse quality of life. Low is good. High is bad. Each of the dots is a real person (maybe those should disappear?). The line represents the typical rate of PD progression over time. Color scheme of different degrees of quality of life can change, but the general concept seems to be working. (see updated version at the bottom of the www.VELQAN.org website)We need to combine the exercise data from here. This poster was essentially my attempt at an infographic for scientists:https://files.brindlehost.net/static/7a2c91e0b4/t/3d8e55f1a0/1482209931245/TRX2017+Meals.pdf. The updated data is in the uploaded figure below. Please use this list/ verbage!I don't necessarily need to stick to red=bad, green=good, but that's the best I've been able to come up with to communicate all this. I can get the actual data output later, but it might be nice to be able to demonstrate intensity. Veggies are quite a bit better than spices. Loneliness is much, much worse than pasta. This is the original published data. We have updated data and want to turn it into an infographic (while we work on a new manuscript).https://www.quorvelpress.com/journals/jcrt/2017/8127439/
Target Market(s)
Individuals age 40-80 with Parkinson's disease (and their friends & family members).
Neurologists should be handing this out in their offices.
When patients ask their physician about nutrition, etc., we want this to be the 1-pg handout they give them.
Industry/Entity Type
Medicine
Font styles to use
Colors
Designer to choose colors to be used in the design.
Requirements
Must have
- VEL-QAN scale (www.VELQAN.org)-- use this picture on top. OK to change color.
- Lists foods/ activities associated with different rates of progression
- Title: "Food, Friends, and Exercise: Lifestyle Associations with PD Progression"
- Legend/ disclaimer (smaller font):
- "All results were adjusted for age, gender, and years since diagnosis. Total sample size: 1600+
- Based on the methods described in publication: "Effects of Meal Timing and Herbal Intake on Tremor Course" [Orvanto TJ et al, Clin Neuro Rehab Rev 2017], an updated analysis was performed on data on 7 May 2019. (N >1600)"
- "VEL-QAN scores available at www.VELQAN.org"
- Must fit on a single 8.5 x 11" page.
Nice to have
- The background should be white-- I want neurologists/ physicians downloading it, printing it, and distributing to patients. I don't want to waste ink.
- Logo for Kellworth University and/or the logo for the "HOLT Path MX" Study. I like the KU emblem in one corner and the picture at the top of this website: www.VELQAN.org
- Would be nice if it could be understood between cultures and/ or easily translated.
- Would be nice if we could invite people to participate in the study!
- "To learn about joining the study, please to www.HOLTPathMX.kellworth.edu"
Should not have
- Pictures of overweight people, or the impression that a muscular white guy is the ideal. I want to leave room for diversity and flexible interpretation.
- Too much text- a good-sized portion of this group will have poor vision and/or dementia. Needs to be simple.
- I like the simplicity of "Good" and "Bad"... don't love the labels. Seems to 'jugdgy'. Maybe "Encourage" and "Avoid" OR "Positive" and "Negative"

```html
<!DOCTYPE html>
<html lang="en">
<head>
<meta charset="utf-8">
<title>Foods, Friends &amp; Exercise: Lifestyle Associations with Parkinson Progression</title>
<link rel="stylesheet" href="https://fonts.googleapis.com/css2?family=Mulish:wght@400;600;700;800&display=swap">
<style>
  :root {
    --ink: #1d1d1d;
    --frame: #a8423a;
    --avoid: #b5665a;
    --encourage: #7ab648;
    --band-poor: #e8d3d5;
    --band-fair: #e6b092;
    --band-good: #aebfdd;
    --band-excellent: #cfe0b5;
    --trend: #b85450;
    --paper: #ffffff;
    --uni: #8a2a1f;
    --study: #5159a6;
    --study-fill: #a9cdee;
  }
  * { box-sizing: border-box; margin: 0; padding: 0; }
  html, body { width: 1200px; height: 936px; overflow: hidden; background: var(--paper); }
  body { font-family: "Mulish", sans-serif; color: var(--ink); position: relative; }

  .frame {
    position: absolute; left: 10px; top: 11px; width: 1177px; height: 907px;
    border: 1.5px solid var(--frame); border-radius: 22px;
  }
  .title {
    position: absolute; left: 0; top: 26px; width: 1200px; text-align: center;
    font-size: 36px; font-weight: 800; line-height: 43px; letter-spacing: 0.3px;
  }
  .chart { position: absolute; left: 0; top: 0; width: 1200px; height: 936px; }
  .chart text { font-family: "Mulish", sans-serif; fill: var(--ink); }

  .findings { position: absolute; left: 0; top: 0; }
  .icon { position: absolute; width: 36px; height: 36px; }
  .list { position: absolute; list-style: none; font-size: 15px; line-height: 18.7px; }
  .list li { position: relative; padding-left: 13px; white-space: nowrap; }
  .list li::before {
    content: ""; position: absolute; left: 0; top: 5px; width: 8px; height: 8px; border-radius: 50%;
  }
  .list.avoid li::before { background: var(--avoid); }
  .list.encourage li::before { background: var(--encourage); }

  .method {
    position: absolute; left: 133px; top: 656px; width: 638px;
    font-size: 15.4px; line-height: 20px; text-align: justify;
  }
  .method h2 { font-size: 15.4px; font-weight: 800; line-height: 20px; }
  .method p + p { margin-top: 20px; }

  .partner { position: absolute; text-align: center; font-size: 12px; font-weight: 700; line-height: 14px; color: var(--ink); }
  .partner .mark { display: block; margin: 0 auto 6px; border-radius: 50%; }
  .partner.university .mark { width: 96px; height: 96px; background: var(--uni); }
  .partner.study .mark { width: 96px; height: 96px; background: var(--study-fill); border: 10px solid var(--study); }

  .footnote {
    position: absolute; left: 0; top: 897px; width: 1200px; text-align: center; font-size: 13.6px;
  }
</style>
</head>
<body>
  <div class="frame"></div>
  <h1 class="title">Foods, Friends &amp; Exercise:<br>Lifestyle Associations with Parkinson Progression</h1>

  <svg class="chart" viewBox="0 0 1500 1170" aria-label="VEL-QAN score by years since diagnosis">
    <text x="547" y="214" font-size="27" font-weight="700" text-anchor="middle">Patient-Reported Outcomes in PD (VEL-QAN)</text>

    <rect x="174" y="240" width="784" height="187" fill="var(--band-poor)"/>
    <rect x="174" y="427" width="784" height="91" fill="var(--band-fair)"/>
    <rect x="174" y="518" width="784" height="92" fill="var(--band-good)"/>
    <rect x="174" y="610" width="784" height="90" fill="var(--band-excellent)"/>

    <g stroke="#fff" stroke-width="2">
      <line x1="174" y1="427" x2="958" y2="427"/>
      <line x1="174" y1="518" x2="958" y2="518"/>
      <line x1="174" y1="610" x2="958" y2="610"/>
      <line x1="174" y1="336" x2="958" y2="336"/>
      <line x1="318" y1="240" x2="318" y2="700"/>
      <line x1="463" y1="240" x2="463" y2="700"/>
      <line x1="608" y1="240" x2="608" y2="700"/>
      <line x1="753" y1="320" x2="753" y2="700"/>
      <line x1="897" y1="240" x2="897" y2="700"/>
    </g>

    <polygon points="174,578 958,364 958,428 174,586" fill="#fff" opacity="0.62"/>
    <line x1="182" y1="582" x2="946" y2="399" stroke="var(--trend)" stroke-width="4.5" stroke-dasharray="13 8"/>

    <rect x="637" y="255" width="233" height="52" fill="#fff"/>
    <polygon points="738,307 768,307 753,321" fill="#fff"/>
    <text x="752" y="291" font-size="28" font-weight="700" text-anchor="middle">Quality of Life</text>

    <rect x="725" y="340" width="62" height="28" fill="var(--band-poor)"/>
    <text x="757" y="363" font-size="24" font-weight="700" text-anchor="middle">Poor</text>
    <rect x="724" y="474" width="58" height="28" fill="var(--band-fair)"/>
    <text x="752" y="497" font-size="24" font-weight="700" text-anchor="middle">Fair</text>
    <rect x="715" y="550" width="76" height="28" fill="var(--band-good)"/>
    <text x="752" y="573" font-size="24" font-weight="700" text-anchor="middle">Good</text>
    <rect x="692" y="638" width="124" height="28" fill="var(--band-excellent)"/>
    <text x="754" y="661" font-size="24" font-weight="700" text-anchor="middle">Excellent</text>

    <g font-size="24" font-weight="700" text-anchor="end">
      <text x="160" y="249">2,500</text>
      <text x="160" y="345">2,000</text>
      <text x="160" y="432">1,500</text>
      <text x="160" y="526">1,000</text>
      <text x="160" y="618">500</text>
      <text x="150" y="705">0</text>
    </g>
    <g font-size="24" font-weight="700" text-anchor="middle">
      <text x="175" y="732">0</text>
      <text x="316" y="732">5</text>
      <text x="463" y="732">10</text>
      <text x="608" y="732">15</text>
      <text x="753" y="732">20</text>
      <text x="895" y="732">25</text>
    </g>
    <text x="562" y="778" font-size="29" font-weight="700" text-anchor="middle">Years Since Diagnosis</text>
    <text transform="translate(66 462) rotate(-90)" font-size="29" font-weight="700" text-anchor="middle">VEL-QAN Score</text>
  </svg>

  <section class="findings">
    <svg class="icon" style="left:797px;top:165px" viewBox="0 0 36 36" aria-hidden="true">
      <circle cx="18" cy="18" r="17" fill="var(--avoid)"/><circle cx="18" cy="18" r="13" fill="none" stroke="#fff" stroke-width="1.5"/>
      <circle cx="18" cy="14" r="4" fill="#fff"/><path d="M11 25a7 6 0 0 1 14 0z" fill="#fff"/>
    </svg>
    <ul class="list avoid" style="left:846px;top:155px">
      <li>“I’m overweight.”</li><li>“I’m lonely.”</li><li>“I have a lot of stress.”</li>
    </ul>

    <svg class="icon" style="left:797px;top:246px" viewBox="0 0 36 36" aria-hidden="true">
      <circle cx="18" cy="18" r="17" fill="var(--avoid)"/><circle cx="18" cy="18" r="13" fill="none" stroke="#fff" stroke-width="1.5"/>
      <path d="M12 12l12 12M24 12l-12 12" stroke="#fff" stroke-width="2.2" stroke-linecap="round"/>
    </svg>
    <ul class="list avoid" style="left:845px;top:225px">
      <li>Dairy</li><li>Beef</li><li>Chicken</li><li>Soda</li>
    </ul>
    <ul class="list avoid" style="left:946px;top:225px">
      <li>Fried foods</li><li>Canned fruits</li><li>Canned vegetables</li><li>Frozen vegetables</li>
    </ul>

    <svg class="icon" style="left:797px;top:309px" viewBox="0 0 36 36" aria-hidden="true">
      <circle cx="18" cy="18" r="17" fill="var(--avoid)"/><circle cx="18" cy="18" r="13" fill="none" stroke="#fff" stroke-width="1.5"/>
      <path d="M18 26l-7-7a4 4 0 0 1 7-5a4 4 0 0 1 7 5z" fill="#fff"/>
      <path d="M10 19h5l2-3 2 5 2-2h5" fill="none" stroke="var(--avoid)" stroke-width="1.4"/>
    </svg>
    <ul class="list avoid" style="left:846px;top:313px">
      <li>Minimal benefit associated to<br>0-2 days/week of exercise</li>
    </ul>

    <svg class="icon" style="left:797px;top:389px" viewBox="0 0 36 36" aria-hidden="true">
      <circle cx="18" cy="18" r="17" fill="var(--encourage)"/><circle cx="18" cy="18" r="13" fill="none" stroke="#fff" stroke-width="1.5"/>
      <circle cx="18" cy="14" r="4" fill="#fff"/><path d="M11 25a7 6 0 0 1 14 0z" fill="#fff"/>
    </svg>
    <ul class="list encourage" style="left:844px;top:366px">
      <li>“I have lots of friends.”</li><li>“I try to eat organic when possible.”</li><li>“I cook most of my own meals.”</li><li>“I practice stress management.”</li>
    </ul>

    <svg class="icon" style="left:797px;top:486px" viewBox="0 0 36 36" aria-hidden="true">
      <circle cx="18" cy="18" r="17" fill="var(--encourage)"/><circle cx="18" cy="18" r="13" fill="none" stroke="#fff" stroke-width="1.5"/>
      <path d="M12 12l12 12M24 12l-12 12" stroke="#fff" stroke-width="2.2" stroke-linecap="round"/>
    </svg>
    <ul class="list encourage" style="left:845px;top:453px">
      <li>Fresh vegetables</li><li>Olive &amp; coconut oil</li><li>Nuts &amp; seeds</li><li>Non-fried fish</li><li>Green tea</li>
    </ul>
    <ul class="list encourage" style="left:1031px;top:453px">
      <li>Fresh fruit</li><li>Fresh herbs</li><li>Spices</li><li>Wine</li>
    </ul>

    <svg class="icon" style="left:797px;top:564px" viewBox="0 0 36 36" aria-hidden="true">
      <circle cx="18" cy="18" r="17" fill="var(--encourage)"/><circle cx="18" cy="18" r="13" fill="none" stroke="#fff" stroke-width="1.5"/>
      <path d="M18 26l-7-7a4 4 0 0 1 7-5a4 4 0 0 1 7 5z" fill="#fff"/>
      <path d="M10 19h5l2-3 2 5 2-2h5" fill="none" stroke="var(--encourage)" stroke-width="1.4"/>
    </svg>
    <ul class="list encourage" style="left:846px;top:554px">
      <li>7 days/week of exercise is better than 6</li><li>6 days/week of exercise is better than 5…</li><li>Trend continues to 3 days/week</li>
    </ul>
  </section>

  <section class="method">
    <h2>Measuring PD Progression</h2>
    <p>Individuals with Parkinson's are asked to describe the severity of 34 common symptoms. 0= healthy - 100= severe. High scores are associated with a lower reported quality of life. The lower your VEL-QAN score, the better!</p>
    <p>HOLT Path MX is an ongoing "big data" study designed to describe modifiable variables associated with RATE of progression. Results presented here are based on data collected between 2012-2019. All analyses were performed according to methods described in <em>Effects of Meal Timing and Herbal Intake on Tremor Course</em> [Orvanto TJ, 2017]."</p>
  </section>

  <div class="partner university" style="left:868px;top:708px;width:126px">
    <span class="mark"></span>Kellworth University
  </div>
  <div class="partner study" style="left:1014px;top:702px;width:126px">
    <span class="mark"></span>HOLT Path MX
  </div>

  <p class="footnote">All results adjusted for age, gender, and years since diagnosis. Total sample size: 1600+. Updated dataset as of 27 May 2019.</p>
</body>
</html>
```